Illustrate a statistic and its significance

Please create a graphical representation of the success rate of the Lanton Procedure for our website. The Lanton Procedure has a success rate of 80%. This means the procedure is successful for 8 out of every 10 people. An 80% success rate by itself is great. However, it's even more impressive when you consider that the only people we perform this procedure on are patients who have exhausted conventional treatment options for migraines and headaches. I would really like to emphasize both the success rate and the type of patients we are successful in treating with this procedure.
For example, you could create an illustration of outlines of 10 people with 8 of them shaded in, which would represent an 80% success rate. Then, underneath this image, you could add a bullet list of the types of treatments patients (such as the 10 figures in the image) have tried before coming to us/having this procedure, which include the following:
Prescription medications
Trigger point injections
Nerve blocks
Migraine surgery
Velquin
Chiropractic care
Physical therapy
Biofeedback
Massage
Acupuncture
Or maybe there is another/better way to represent this statistic graphically? I'm just looking for an effective illustration of this important statistic and its significance.
Our brand colors are red (#fd444a) and blue (#214170)
Thank you!
Target Market(s)
People who suffer from chronic migraines and headaches
Industry/Entity Type
Healthcare/Medical
Other font styles liked:
- Athiti

```html
<!DOCTYPE html>
<html lang="en">
<head>
<meta charset="utf-8">
<title>Lanton Procedure – 80% Success</title>
<link rel="stylesheet" href="https://fonts.googleapis.com/css2?family=Source+Sans+3:wght@400;600;700&display=swap">
<style>
  :root {
    --brand-red: #ef4850;
    --brand-blue: #1f4170;
    --tile-pink: #fad9dd;
    --paper: #ffffff;
    --page: #ffffff;
  }
  * { box-sizing: border-box; margin: 0; padding: 0; }
  html, body {
    width: 1200px; height: 1068px; overflow: hidden;
    background: var(--page);
    font-family: "Source Sans 3", "Myriad Pro", sans-serif;
  }
  .canvas { position: relative; width: 1200px; height: 1068px; }
  .card {
    position: absolute; left: 16px; top: 32px; width: 1141px; height: 991px;
    background: var(--paper);
    box-shadow: 10px 12px 14px rgba(0,0,0,0.35);
  }
  .pill {
    position: absolute; top: 78px; height: 84px; border-radius: 28px;
    display: flex; align-items: center; justify-content: center;
    font-weight: 700; text-transform: uppercase; line-height: 1;
  }
  .pill--name {
    left: 96px; width: 473px; background: var(--brand-blue); color: var(--brand-red);
    font-size: 50px; letter-spacing: -1px;
  }
  .pill--stat {
    left: 599px; width: 469px; background: var(--brand-red); color: var(--brand-blue);
    font-size: 56px; letter-spacing: -1px;
  }
  .patient {
    position: absolute; width: 175px; height: 176px; border-radius: 32px;
    border: 2px solid var(--brand-blue); overflow: hidden;
  }
  .patient--success { background: var(--tile-pink); }
  .patient--unresolved { background: var(--paper); }
  .patient__figure {
    position: absolute; left: 36px; right: 36px; top: 22px; bottom: 0;
    border-radius: 46px 46px 0 0;
  }
  .patient--success .patient__figure { background: linear-gradient(180deg, var(--brand-blue), var(--brand-blue)); opacity: 0.92; }
  .patient--unresolved .patient__figure { background: var(--brand-red); }
  .treatments {
    position: absolute; left: 399px; top: 585px; width: 400px; height: 408px;
    border: 2px solid var(--brand-blue); border-radius: 0 0 41px 41px;
    overflow: hidden; background: var(--paper);
  }
  .treatments__title {
    height: 50px; background: var(--brand-red); color: #fff;
    font-weight: 400; font-size: 33px; letter-spacing: -0.6px;
    display: flex; align-items: center; justify-content: center;
  }
  .treatments__title span { display: inline-block; transform: scaleX(0.9); white-space: nowrap; }
  .treatments__list { list-style: none; position: absolute; left: 70px; top: 66px; }
  .treatments__item {
    display: flex; align-items: center; height: 33px;
    font-size: 23px; font-weight: 600; color: var(--brand-blue);
  }
  .treatments__mark { width: 19px; height: 19px; margin-right: 10px; flex: none; }
</style>
</head>
<body>
<div class="canvas">
  <div class="card"></div>

  <div class="pill pill--name">Lanton Procedure</div>
  <div class="pill pill--stat">80% Success</div>

  <div class="patients">
    <div class="patient patient--success" style="left:98px;top:180px"><div class="patient__figure" role="img" aria-label="Patient silhouette, successfully treated"></div></div>
    <div class="patient patient--success" style="left:298px;top:180px"><div class="patient__figure" role="img" aria-label="Patient silhouette, successfully treated"></div></div>
    <div class="patient patient--success" style="left:496px;top:180px"><div class="patient__figure" role="img" aria-label="Patient silhouette, successfully treated"></div></div>
    <div class="patient patient--success" style="left:697px;top:181px"><div class="patient__figure" role="img" aria-label="Patient silhouette, successfully treated"></div></div>
    <div class="patient patient--success" style="left:894px;top:181px"><div class="patient__figure" role="img" aria-label="Patient silhouette, successfully treated"></div></div>
    <div class="patient patient--success" style="left:99px;top:373px"><div class="patient__figure" role="img" aria-label="Patient silhouette, successfully treated"></div></div>
    <div class="patient patient--success" style="left:300px;top:373px"><div class="patient__figure" role="img" aria-label="Patient silhouette, successfully treated"></div></div>
    <div class="patient patient--success" style="left:498px;top:373px"><div class="patient__figure" role="img" aria-label="Patient silhouette, successfully treated"></div></div>
    <div class="patient patient--unresolved" style="left:698px;top:375px"><div class="patient__figure" role="img" aria-label="Patient silhouette, not resolved"></div></div>
    <div class="patient patient--unresolved" style="left:898px;top:375px"><div class="patient__figure" role="img" aria-label="Patient silhouette, not resolved"></div></div>
  </div>

  <section class="treatments">
    <h2 class="treatments__title"><span>UNSUCCESFUL TREATMENTS</span></h2>
    <ul class="treatments__list">
      <li class="treatments__item"><svg class="treatments__mark" viewBox="0 0 19 19"><rect width="19" height="19" fill="var(--brand-red)"/><path d="M5 3.5 L14 15.5 M14 3.5 L5 15.5" stroke="#fff" stroke-width="2.4"/></svg>Prescription medications</li>
      <li class="treatments__item"><svg class="treatments__mark" viewBox="0 0 19 19"><rect width="19" height="19" fill="var(--brand-red)"/><path d="M5 3.5 L14 15.5 M14 3.5 L5 15.5" stroke="#fff" stroke-width="2.4"/></svg>Trigger point injections</li>
      <li class="treatments__item"><svg class="treatments__mark" viewBox="0 0 19 19"><rect width="19" height="19" fill="var(--brand-red)"/><path d="M5 3.5 L14 15.5 M14 3.5 L5 15.5" stroke="#fff" stroke-width="2.4"/></svg>Nerve blocks</li>
      <li class="treatments__item"><svg class="treatments__mark" viewBox="0 0 19 19"><rect width="19" height="19" fill="var(--brand-red)"/><path d="M5 3.5 L14 15.5 M14 3.5 L5 15.5" stroke="#fff" stroke-width="2.4"/></svg>Migraine surgery</li>
      <li class="treatments__item"><svg class="treatments__mark" viewBox="0 0 19 19"><rect width="19" height="19" fill="var(--brand-red)"/><path d="M5 3.5 L14 15.5 M14 3.5 L5 15.5" stroke="#fff" stroke-width="2.4"/></svg>Velquin</li>
      <li class="treatments__item"><svg class="treatments__mark" viewBox="0 0 19 19"><rect width="19" height="19" fill="var(--brand-red)"/><path d="M5 3.5 L14 15.5 M14 3.5 L5 15.5" stroke="#fff" stroke-width="2.4"/></svg>Chiropractic care</li>
      <li class="treatments__item"><svg class="treatments__mark" viewBox="0 0 19 19"><rect width="19" height="19" fill="var(--brand-red)"/><path d="M5 3.5 L14 15.5 M14 3.5 L5 15.5" stroke="#fff" stroke-width="2.4"/></svg>Physical therapy</li>
      <li class="treatments__item"><svg class="treatments__mark" viewBox="0 0 19 19"><rect width="19" height="19" fill="var(--brand-red)"/><path d="M5 3.5 L14 15.5 M14 3.5 L5 15.5" stroke="#fff" stroke-width="2.4"/></svg>Biofeedback</li>
      <li class="treatments__item"><svg class="treatments__mark" viewBox="0 0 19 19"><rect width="19" height="19" fill="var(--brand-red)"/><path d="M5 3.5 L14 15.5 M14 3.5 L5 15.5" stroke="#fff" stroke-width="2.4"/></svg>Massage</li>
      <li class="treatments__item"><svg class="treatments__mark" viewBox="0 0 19 19"><rect width="19" height="19" fill="var(--brand-red)"/><path d="M5 3.5 L14 15.5 M14 3.5 L5 15.5" stroke="#fff" stroke-width="2.4"/></svg>Acupuncture</li>
    </ul>
  </section>
</div>
</body>
</html>
```